Halvorne Ridge Partners

Please look at the logo that we've just received and based on it provide us with the business card designs.

Industry/Entity Type

Business

Requirements
Must have
• Dummy text, so later on we can add the exact names and titles.

```html
<!DOCTYPE html>
<html lang="en">
<head>
<meta charset="utf-8">
<title>Halvorne Ridge Partners – Business Card</title>
<link rel="stylesheet" href="https://fonts.googleapis.com/css2?family=Cinzel:wght@400&family=Roboto+Condensed:wght@400;500&display=swap">
<style>
  :root {
    --backdrop: #0b5f8e;
    --card: #ffffff;
    --brand-blue: #1e3f9c;
    --ink-grey: #555a60;
  }
  * { margin: 0; padding: 0; box-sizing: border-box; }
  html, body {
    width: 1200px;
    height: 1200px;
    overflow: hidden;
    background: var(--backdrop);
  }
  .business-card {
    position: absolute;
    left: 182px;
    top: 362px;
    width: 839px;
    height: 476px;
    background: var(--card);
  }
  .person {
    position: absolute;
    right: 53px;
    top: 52px;
    text-align: right;
  }
  .person-name {
    font-family: "Cinzel", serif;
    font-weight: 400;
    font-size: 40px;
    line-height: 1;
    color: var(--brand-blue);
    letter-spacing: -0.5px;
  }
  .person-title {
    margin-top: 14px;
    font-family: "Roboto Condensed", sans-serif;
    font-size: 23px;
    line-height: 1;
    color: var(--ink-grey);
    letter-spacing: 0.3px;
  }
  .brand {
    position: absolute;
    left: 160px;
    top: 196px;
    display: flex;
    align-items: center;
    gap: 16px;
  }
  .brand-mark {
    width: 24px;
    height: 24px;
    background: var(--brand-blue);
  }
  .brand-name {
    font-family: "Roboto Condensed", sans-serif;
    font-weight: 500;
    font-size: 38px;
    line-height: 1;
    color: var(--brand-blue);
  }
  .contact-list {
    position: absolute;
    left: 246px;
    top: 310px;
    list-style: none;
  }
  .contact-item {
    display: flex;
    align-items: center;
    height: 40px;
    font-family: "Roboto Condensed", sans-serif;
    font-size: 23px;
    color: var(--ink-grey);
  }
  .contact-icon {
    width: 26px;
    height: 26px;
    margin-right: 13px;
    flex: none;
    fill: none;
    stroke: var(--brand-blue);
  }
</style>
</head>
<body>
  <main class="business-card">
    <header class="person">
      <h1 class="person-name">DANIEL ROARKE</h1>
      <p class="person-title">ASSET MANAGER</p>
    </header>

    <div class="brand">
      <span class="brand-mark"></span>
      <span class="brand-name">Halvorne Ridge Partners</span>
    </div>

    <ul class="contact-list">
      <li class="contact-item">
        <svg class="contact-icon" viewBox="0 0 26 26" aria-hidden="true">
          <path d="M8 3 L11 3 L12 8 L9.5 9.5 Q11 15 15.5 18.5 L17.5 16.5 L22 18 L22 21 Q20 23.5 16 22 Q6 17 4.5 7 Q5 4 8 3 Z" fill="var(--brand-blue)" stroke="none"/>
        </svg>
        <span>555.014.0127</span>
      </li>
      <li class="contact-item">
        <svg class="contact-icon" viewBox="0 0 26 26" aria-hidden="true">
          <circle cx="13" cy="13" r="4.5" stroke-width="2.4"/>
          <path d="M17.5 9 V15 Q17.5 18 20 18 Q23 18 23 13 A10 10 0 1 0 18 21.7" stroke-width="2.4"/>
        </svg>
        <span>danielroarke@examplemail.com</span>
      </li>
      <li class="contact-item">
        <svg class="contact-icon" viewBox="0 0 26 26" aria-hidden="true">
          <circle cx="13" cy="13" r="10.5" stroke-width="1.6"/>
          <ellipse cx="13" cy="13" rx="4.5" ry="10.5" stroke-width="1.4"/>
          <line x1="2.5" y1="13" x2="23.5" y2="13" stroke-width="1.4"/>
          <line x1="4.5" y1="7.5" x2="21.5" y2="7.5" stroke-width="1.4"/>
          <line x1="4.5" y1="18.5" x2="21.5" y2="18.5" stroke-width="1.4"/>
        </svg>
        <span>halvorneassets.com</span>
      </li>
    </ul>
  </main>
</body>
</html>
```